Quillfern Nightclub Flyer (Updated)

Flyer for facebook, square is fine, or rectangular. Here is the text:
QUILLFERN
Nightclub + Lounge
presents

SPLIT DECK WEDNESDAY
Nov 29 2018

CLUB FLOOR:
GORDY B2B RALPH
THEODORE BRUSKVIK

LOUNGE:
OTIS B2B HALF TIDE
COPPER FENWICK

Powered by HALVERN Acoustics
4716 Larchmere Avenue 21+ 9pm-2am
quillfernvenue-example.com for VIP booth inquiries

Target Market(s)

Nightclub

Industry/Entity Type

Night Club

Font styles to use
Sans Serif

Colors

Designer to choose colors to be used in the design.

Requirements
Must have
• All the text listed, and plz keep the theme of the attached files. We want to stay consistent with the Quillfern brand
Nice to have
• Try to stay with the theme from the attachments
Should not have
• Dont' stray to far from the general theme we have from the attachments

```html
<!DOCTYPE html>
<html lang="en">
<head>
<meta charset="utf-8">
<title>Quillfern Nightclub – Split Deck Wednesday</title>
<link rel="stylesheet" href="https://fonts.googleapis.com/css2?family=Bodoni+Moda:wght@400;500&family=Playfair+Display:wght@700&family=Montserrat:wght@300;400&family=Oswald:wght@600&display=swap">
<style>
  :root {
    --page: #ffffff;
    --card-light: #e7e8ea;
    --card-dark: #b8babd;
    --ink: #1d1b1c;
    --gold: #b8925a;
    --gold-light: #dcb984;
    --label: #ffffff;
    --fine: #55575a;
    --rule: #8d8f92;
  }
  * { margin: 0; padding: 0; box-sizing: border-box; }
  html, body { width: 1200px; height: 1200px; overflow: hidden; background: var(--page); }
  .flyer {
    position: absolute; left: 214px; top: 398px; width: 774px; height: 406px;
    background: linear-gradient(90deg, var(--card-light) 0%, #d6d7d9 55%, var(--card-dark) 100%);
    overflow: hidden;
  }
  .ornament { position: absolute; left: 0; top: 0; width: 774px; height: 406px; }
  .brand {
    position: absolute; left: 0; width: 774px; top: 38px; text-align: center;
    font-family: "Bodoni Moda", serif; font-weight: 400; font-size: 62px; line-height: 1;
    color: var(--ink); letter-spacing: 1px;
  }
  .tagline {
    position: absolute; left: 0; width: 774px; text-align: center;
    font-family: "Montserrat", sans-serif; font-weight: 400; font-size: 14px;
    letter-spacing: 3.2px; color: var(--ink); line-height: 1;
  }
  .tagline.venue { top: 112px; }
  .tagline.presents { top: 128px; }
  .date-box {
    position: absolute; left: 380px; top: 176px; width: 139px; height: 37px;
    border: 1px solid var(--gold-light);
    display: flex; align-items: center; justify-content: center;
    font-family: "Bodoni Moda", serif; font-weight: 500; font-size: 20px; color: var(--gold);
  }
  .event-title {
    position: absolute; left: 530px; top: 183px;
    font-family: "Playfair Display", serif; font-weight: 700; font-size: 16px;
    color: var(--ink); letter-spacing: 0.6px; white-space: nowrap;
  }
  .title-rule { position: absolute; left: 530px; top: 208px; width: 194px; height: 8px; }
  .lineup-label {
    position: absolute; right: 256px; text-align: right;
    font-family: "Oswald", sans-serif; font-weight: 600; font-size: 11px;
    letter-spacing: 1.2px; color: var(--label); line-height: 1;
  }
  .lineup-names {
    position: absolute; left: 530px;
    font-family: "Montserrat", sans-serif; font-weight: 400; font-size: 14px;
    line-height: 19.5px; color: var(--ink); white-space: nowrap;
  }
  .club-label { top: 236px; }
  .club-names { top: 231px; }
  .lounge-label { top: 292px; }
  .lounge-names { top: 287px; }
  .rule { position: absolute; height: 1px; background: var(--rule); opacity: .6; }
  .rule.top { left: 378px; width: 341px; top: 346px; }
  .rule.bottom { left: 378px; width: 339px; top: 389px; }
  .fine-print {
    position: absolute; left: 385px; font-family: "Montserrat", sans-serif; font-weight: 400;
    font-size: 7.6px; letter-spacing: .6px; color: var(--fine); white-space: nowrap; line-height: 1;
  }
  .fine-print.info { top: 356px; }
  .fine-print.web { top: 370px; }
</style>
</head>
<body>
  <div class="flyer">
    <svg class="ornament" viewBox="0 0 774 406" role="img" aria-label="Gold mandala ornament, quarter circle in the lower left corner">
      <defs>
        <radialGradient id="gold-fill" cx="0" cy="406" r="280" gradientUnits="userSpaceOnUse">
          <stop offset="0" stop-color="#c99e63"/>
          <stop offset="0.75" stop-color="#d9b27a"/>
          <stop offset="1" stop-color="#e9cfa6"/>
        </radialGradient>
      </defs>
      <circle cx="0" cy="406" r="280" fill="url(#gold-fill)"/>
    </svg>

    <h1 class="brand">QUILLFERN</h1>
    <p class="tagline venue">NIGHTCLUB + LOUNGE</p>
    <p class="tagline presents">PRESENTS</p>

    <div class="date-box">NOV. 29. 2018</div>
    <h2 class="event-title">Split Deck Wednesday</h2>
    <svg class="title-rule" viewBox="0 0 194 8">
      <line x1="0" y1="4" x2="178" y2="4" stroke="#8d8f92" stroke-width="0.8"/>
      <circle cx="184" cy="4" r="2.5" fill="none" stroke="#c4a06b" stroke-width="0.9"/>
      <circle cx="191" cy="4" r="1.5" fill="#c4a06b"/>
    </svg>

    <p class="lineup-label club-label">CLUB FLOOR:</p>
    <p class="lineup-names club-names">GORDY B2B RALPH<br>THEODORE BRUSKVIK</p>

    <p class="lineup-label lounge-label">LOUNGE:</p>
    <p class="lineup-names lounge-names">OTIS B2B HALF TIDE<br>COPPER FENWICK</p>

    <div class="rule top"></div>
    <p class="fine-print info">POWERED BY: HALVERN ACOUSTICS 4716 LARCHMERE AVENUE 21+ 9PM-2AM</p>
    <p class="fine-print web">QUILLFERNVENUE-EXAMPLE.COM FOR VIP BOOTH INQUIRIES</p>
    <div class="rule bottom"></div>
  </div>
</body>
</html>
```